Poster of Insipirational Quotes

Attached is a list of leadership quotes from Harold Brenwick. I would like a poster made, incorporating whatever design elements you like, potentially including Harold's face, and one or more of the quotes. I intend to print this out in A3 or larger to hang on my wall.

The quotes are:

Being responsible sometimes means pissing people off.

The day soldiers stop bringing you their problems is the day you have stopped leading them.

Don't be buffaloed by experts and elites. Experts often possess more data than judgment. Elites can become so inbred that they produce hemophiliacs who bleed to death as soon as they are nicked by the real world.

Don't be afraid to challenge the pros, even in their own backyard.

Never neglect details. When everyone's mind is dulled or distracted the leader must be doubly vigilant.

You don't know what you can get away with until you try.

Keep looking below surface appearances. Don't shrink from doing so (just) because you might not like what you find.

Organization doesn't really accomplish anything. Plans don't accomplish anything, either. Theories of management don't much matter. Endeavors succeed or fail because of the people involved. Only by attracting the best people will you accomplish great deeds.

Organization charts and fancy titles count for next to nothing.

Never let your ego get so close to your position that when your position goes, your ego goes with it.

Fit no stereotypes. Don't chase the latest management fads. The situation dictates which approach best accomplishes the team's mission.

Perpetual optimism is a force multiplier.

Look for intelligence and judgment, and most critically, a capacity to anticipate, to see around corners. Also look for loyalty, integrity, a high energy drive, a balanced ego, and the drive to get things done.

Great leaders are almost always great simplifiers, who can cut through argument, debate and doubt, to offer a solution everybody can understand.

The commander in the field is always right and the rear echelon is wrong, unless proved otherwise.

Have fun in your command. Don't always run at a breakneck pace. Take leave when you've earned it: Spend time with your families. Corollary: surround yourself with people who take their work seriously, but not themselves, those who work hard and play hard.

Command is lonely.

Leadership is the art of accomplishing more than the science of management
says is possible.

I need to modify the specification based on the designs that I've seen.

Executive Office

Designer to choose colors to be used in the design.

• Quotes

```html
<!DOCTYPE html>
<html lang="en">
<head>
<meta charset="utf-8">
<title>Harold Brenwick Leadership Quotes Posters</title>
<link rel="stylesheet" href="https://fonts.googleapis.com/css2?family=Marcellus+SC&display=swap">
<style>
  :root {
    --backdrop: #ececec;
    --paper: #ffffff;
    --ink: #111111;
    --portrait-light: #f4f4f4;
    --portrait-mid: #d6d6d6;
    --portrait-dark: #bdbdbd;
  }
  * { margin: 0; padding: 0; box-sizing: border-box; }
  html, body {
    width: 1200px; height: 923px; overflow: hidden;
    background: var(--backdrop);
  }
  .canvas { position: relative; width: 1200px; height: 923px; }
  .poster {
    position: absolute; top: 109px;
    width: 554px; height: 783px;
    background: var(--paper);
    overflow: hidden;
  }
  .poster--left { left: 37px; }
  .poster--right { left: 612px; }
  .portrait {
    position: absolute; left: 0; top: 0; width: 554px; height: 783px;
  }
  .quote {
    position: absolute;
    width: 176px; margin-left: -88px;
    font-family: "Marcellus SC", serif;
    color: var(--ink);
    text-align: center;
    text-transform: uppercase;
    font-size: 15px;
  }
  .quote--dense { font-size: 14px; letter-spacing: -0.3px; }
  .quote--tiny { font-size: 13px; letter-spacing: -0.4px; width: 184px; margin-left: -92px; }
</style>
</head>
<body>
<main class="canvas">

  <section class="poster poster--left" aria-label="Leadership quotes poster one">
    <svg class="portrait" role="img" aria-label="Faint greyscale portrait of Harold Brenwick behind the quotes" viewBox="0 0 554 783">
      <defs>
        <radialGradient id="portraitLeft" cx="0.5" cy="0.62" r="0.6">
          <stop offset="0" stop-color="var(--portrait-mid)"/>
          <stop offset="0.6" stop-color="var(--portrait-light)"/>
          <stop offset="1" stop-color="var(--paper)"/>
        </radialGradient>
      </defs>
      <rect width="554" height="783" fill="url(#portraitLeft)"/>
    </svg>

    <p class="quote" style="left:92px; top:46px; line-height:25.8px;">"Being<br>responsible<br>sometimes<br>means<br>pissing<br>people<br>off."</p>
    <p class="quote quote--dense" style="left:277px; top:20px; line-height:15px;">"Don't be<br>buffaloed by<br>experts and<br>elites. Experts<br>often possess<br>more data than<br>judgment. Elites<br>can become so<br>inbred that they<br>produce<br>hemophiliacs who<br>bleed to death as<br>soon as they are<br>nicked by the<br>real world."</p>
    <p class="quote" style="left:466px; top:20px; line-height:21.8px;">"The day<br>soldiers<br>stop<br>bringing you<br>their<br>problems is<br>the day you<br>have<br>stopped<br>leading<br>them."</p>

    <p class="quote" style="left:92px; top:290px; line-height:27.7px;">"Don't be<br>afraid to<br>challenge<br>the pros,<br>even in<br>their own<br>backyard."</p>
    <p class="quote" style="left:277px; top:277px; line-height:21.8px;">"Never<br>neglect<br>details. When<br>everyone's<br>mind is dulled<br>or distracted<br>the leader<br>must be<br>doubly<br>vigilant."</p>
    <p class="quote" style="left:466px; top:312px; line-height:25px;">"You don't<br>know what<br>you can<br>get away<br>with until<br>you try."</p>

    <p class="quote" style="left:92px; top:528px; line-height:21.8px;">"Keep looking<br>below<br>surface<br>appearances.<br>Don't shrink<br>from doing<br>so (just)<br>because you<br>might not<br>like what you<br>find."</p>
    <p class="quote quote--tiny" style="left:277px; top:531px; line-height:13.9px;">"Organization<br>doesn't really<br>accomplish<br>anything. Plans<br>don't accomplish<br>anything, either.<br>Theories of<br>management don't<br>much matter.<br>Endeavors succeed<br>or fail because of<br>the people<br>involved. Only by<br>attracting the best<br>people will you<br>accomplish great<br>deeds."</p>
    <p class="quote" style="left:466px; top:557px; line-height:31.4px;">"Organization<br>charts and<br>fancy titles<br>count for<br>next to<br>nothing."</p>
  </section>

  <section class="poster poster--right" aria-label="Leadership quotes poster two">
    <svg class="portrait" role="img" aria-label="Faint greyscale portrait of Harold Brenwick behind the quotes" viewBox="0 0 554 783">
      <defs>
        <radialGradient id="portraitRight" cx="0.5" cy="0.6" r="0.6">
          <stop offset="0" stop-color="var(--portrait-dark)"/>
          <stop offset="0.6" stop-color="var(--portrait-light)"/>
          <stop offset="1" stop-color="var(--paper)"/>
        </radialGradient>
      </defs>
      <rect width="554" height="783" fill="url(#portraitRight)"/>
    </svg>

    <p class="quote" style="left:111px; top:34px; line-height:26.3px;">"Never let your<br>ego get so<br>close to your<br>position that<br>when your<br>position goes,<br>your ego goes<br>with it."</p>
    <p class="quote" style="left:277px; top:20px; line-height:19.8px;">"Fit no<br>stereotypes.<br>Don't chase the<br>latest<br>management<br>fads. The<br>situation<br>dictates which<br>approach best<br>accomplishes<br>the team's<br>mission."</p>
    <p class="quote" style="left:454px; top:53px; line-height:33.7px;">"Perpetual<br>optimism<br>is a<br>force<br>multiplier."</p>

    <p class="quote quote--dense" style="left:113px; top:265px; line-height:17.3px; width:184px; margin-left:-92px;">"Look for<br>intelligence and<br>judgment, and<br>most critically, a<br>capacity to see<br>anticipate, to see<br>around corners.<br>Also look for<br>loyalty, integrity,<br>a high energy<br>drive, a balanced<br>ego, and the<br>drive to get<br>things done."</p>
    <p class="quote" style="left:277px; top:351px; line-height:25.4px;">"Command<br>is<br>lonely."</p>
    <p class="quote" style="left:454px; top:270px; line-height:21.8px;">"Great leaders<br>are almost<br>always great<br>simplifiers, who<br>can cut through<br>argument,<br>debate and<br>doubt, to offer<br>a solution<br>everybody can<br>understand."</p>

    <p class="quote" style="left:111px; top:542px; line-height:21.2px;">"The<br>commander in<br>the field<br>is always right<br>and the rear<br>echelon<br>is wrong,<br>unless<br>proved<br>otherwise."</p>
    <p class="quote" style="left:277px; top:562px; line-height:21.8px;">"Leadership<br>is the art of<br>accomplishing<br>more than the<br>science of<br>management<br>says is<br>possible."</p>
    <p class="quote quote--tiny" style="left:454px; top:528px; line-height:13.9px;">"Have fun in your<br>command. Don't<br>always run at a<br>breakneck pace.<br>Take leave when<br>you've earned it:<br>spend time with<br>your families.<br>Corollary:<br>surround<br>yourself with<br>people who take<br>their work<br>seriously, but not<br>themselves, those<br>who work hard<br>and play hard."</p>
  </section>

</main>
</body>
</html>
```